Re-Design of existing Shopify Website

Hi,

We are looking for a skilled person to work with us on improving the design of our website to make it more user friendly. We are a Makeup brush and makeup accessories company and our current website can be viewed at pillowandfern dot com.We are looking to simplify the layout and make it more modern and mobile friendly.

We have designs in mind which we would like to implement to our site which we feel would work better for us to increase traffic and sales.

We would like the layout to have clear sections for brushes,lashes ,sponge and also our tutorials on the landing page.

Industry/Entity Type

Hair And Beauty

Number of Pages Required

5+ page

Font styles to use
Sans Serif

Colors
b8a6cd
d3a5cc
eea4c8
ffffff
000000

Requirements
Must have
• -Clear ,modern landing page.
• -easy navigation
• -simple design
• -professional design approach
Nice to have
• cross selling pop up
Should not have
• over use of bold colour.

```html
<!DOCTYPE html>
<html lang="en">
<head>
<meta charset="utf-8">
<title>Pillow &amp; Fern — Brushes, Lashes &amp; Sponges</title>
<link href="https://fonts.googleapis.com/css2?family=Open+Sans:wght@300;400;600&display=swap" rel="stylesheet">
<style>
  :root {
    --lavender: #a993c9;
    --lavender-soft: #b8a6cd;
    --ink: #222222;
    --nav: #444444;
    --white: #ffffff;
    --peach: #fde9e0;
    --stone: #eee4dd;
    --rose-icon: #b98a8c;
    --field-line: #c9c3cb;
    --footer: #3b3737;
    --footer-text: #d9d4d4;
  }
  * { box-sizing: border-box; margin: 0; padding: 0; }
  html, body { width: 1200px; height: 2844px; overflow: hidden; }
  body { font-family: "Open Sans", Arial, sans-serif; color: var(--ink); background: var(--white); position: relative; }
  a { text-decoration: none; }

  /* Header */
  .site-header { position: absolute; top: 0; left: 0; width: 1200px; height: 96px; background: var(--white); }
  .brand { position: absolute; left: 84px; top: 22px; font-size: 35px; font-weight: 300; color: var(--ink); letter-spacing: -0.5px; white-space: nowrap; }
  .main-nav { position: absolute; right: 88px; top: 38px; display: flex; gap: 34px; font-size: 17px; text-transform: uppercase; white-space: nowrap; }
  .main-nav a { color: var(--nav); }
  .main-nav a.is-active { color: var(--lavender); }

  /* Hero */
  .hero { position: absolute; top: 96px; left: 0; width: 1200px; height: 591px; }
  .hero-photo { position: absolute; inset: 0; background: linear-gradient(100deg, #2f4256 0%, #3d5166 38%, #6b6f73 62%, #8a7868 80%, #3f3a38 100%); }
  .hero-title { position: absolute; left: 84px; top: 150px; font-size: 39px; line-height: 58px; font-weight: 600; color: var(--white); white-space: nowrap; }
  .hero-title .amp { color: var(--lavender-soft); font-size: 48px; font-weight: 400; }
  .btn-hero { position: absolute; left: 84px; top: 371px; width: 209px; height: 69px; border: 4px solid var(--white); color: var(--white); font-size: 24px; font-weight: 600; display: flex; align-items: center; justify-content: center; text-transform: uppercase; }
  .slider-dots { position: absolute; left: 570px; top: 553px; display: flex; gap: 16px; }
  .slider-dots span { width: 15px; height: 15px; border: 2px solid var(--white); border-radius: 50%; }
  .slider-dots span.is-current { background: var(--white); }

  /* About */
  .about { position: absolute; top: 687px; left: 0; width: 1200px; height: 362px; padding: 50px 87px 0; }
  .section-title { font-size: 31px; font-weight: 600; color: var(--lavender); text-transform: uppercase; }
  .about p { margin-top: 14px; font-size: 22px; line-height: 40px; white-space: nowrap; }
  .btn-outline { display: inline-flex; align-items: center; justify-content: center; border: 3px solid var(--lavender); color: var(--lavender); text-transform: uppercase; font-weight: 600; }
  .about .btn-outline { margin-top: 28px; width: 187px; height: 56px; font-size: 22px; }

  /* Product categories */
  .categories { position: absolute; top: 1049px; left: 0; width: 1200px; height: 602px; }
  .category { position: absolute; top: 0; width: 600px; height: 602px; padding: 30px 87px 0; }
  .category--brushes { left: 0; background: var(--peach); }
  .category--lashes { left: 600px; background: var(--stone); padding-left: 75px; }
  .category h3 { font-size: 23px; font-weight: 600; color: var(--lavender); line-height: 32px; }
  .category-photo { margin-top: 24px; width: 458px; height: 298px; }
  .category--brushes .category-photo { background: linear-gradient(135deg, #c9b2a0 0%, #b78e6c 45%, #8e8a88 100%); }
  .category--lashes .category-photo { background: linear-gradient(135deg, #4d5f86 0%, #8b7060 45%, #2d3f6d 100%); }
  .category p { margin-top: 34px; font-size: 19px; line-height: 27px; width: 440px; }
  .price-tag { margin-top: 24px; width: 156px; height: 44px; border: 2px solid var(--lavender); color: var(--lavender); font-size: 22px; font-weight: 600; display: flex; align-items: center; justify-content: center; }

  /* Highlights */
  .highlights { position: absolute; top: 1651px; left: 0; width: 1200px; height: 405px; }
  .highlight { position: absolute; top: 40px; width: 300px; }
  .highlight-icon { width: 72px; height: 72px; display: block; }
  .highlight h4 { margin-top: 38px; font-size: 20px; line-height: 28px; font-weight: 600; color: var(--lavender); white-space: nowrap; }
  .highlight p { margin-top: 20px; font-size: 19px; line-height: 27px; width: 290px; }
  .highlight .btn-outline { margin-top: 24px; width: 156px; height: 44px; font-size: 18px; border-width: 2px; font-weight: 400; }

  /* Contact */
  .contact { position: absolute; top: 2056px; left: 0; width: 1200px; height: 724px; }
  .contact-photo { position: absolute; inset: 0; background: radial-gradient(ellipse 380px 620px at 880px 360px, #6e5f5c 0%, #4a3a38 55%, transparent 100%), linear-gradient(90deg, #2a2021 0%, #3a2c2c 60%, #2e2425 100%); }
  .contact-title { position: absolute; left: 84px; top: 36px; font-size: 36px; font-weight: 600; color: var(--lavender-soft); text-transform: uppercase; }
  .field-label { position: absolute; font-size: 25px; font-weight: 600; color: var(--lavender-soft); text-transform: uppercase; }
  .field-box { position: absolute; border: 4px solid var(--field-line); border-radius: 4px; }
  .btn-send { position: absolute; left: 87px; top: 624px; width: 233px; height: 56px; border: 4px solid var(--lavender-soft); color: var(--lavender-soft); font-size: 25px; font-weight: 600; display: flex; align-items: center; justify-content: center; text-transform: uppercase; border-radius: 2px; }

  /* Footer */
  .site-footer { position: absolute; top: 2780px; left: 0; width: 1200px; height: 64px; background: var(--footer); color: var(--footer-text); }
  .copyright { position: absolute; left: 86px; top: 18px; font-size: 21px; }
  .social-links { position: absolute; right: 88px; top: 24px; display: flex; gap: 30px; }
  .social-links span { width: 16px; height: 16px; border-radius: 50%; background: var(--footer-text); }
</style>
</head>
<body>

<header class="site-header">
  <div class="brand">Pillow &amp; Fern</div>
  <nav class="main-nav">
    <a class="is-active" href="#">Home</a>
    <a href="#">About</a>
    <a href="#">Brushes</a>
    <a href="#">Lashes</a>
    <a href="#">Sponges</a>
    <a href="#">Tutorials</a>
  </nav>
</header>

<section class="hero">
  <div class="hero-photo" role="img" aria-label="Model with long windswept brown hair against a blue-grey backdrop"></div>
  <h1 class="hero-title">QUALITY BEAUTY : A unique<br>solution for Your<br>Hair <span class="amp">&amp;</span> Beauty.</h1>
  <a class="btn-hero" href="#">Contact Now</a>
  <div class="slider-dots"><span class="is-current"></span><span></span><span></span></div>
</section>

<section class="about">
  <h2 class="section-title">About Us</h2>
  <p>Lorem Ipsum is simply dummy text of the printing and typesetting industry. Lorem Ipsum has<br>been the industry's standard dummy text ever since the 1500s, when an unknown printer took<br>a galley of type and scrambled it to make a type specimen book.</p>
  <a class="btn-outline" href="#">Know More</a>
</section>

<section class="categories">
  <article class="category category--brushes">
    <h3>Brushes</h3>
    <div class="category-photo" role="img" aria-label="Make-up brush set laid out on a soft neutral surface"></div>
    <p>Lorem Ipsum is simply dummy text of the printing and typesetting industry.</p>
    <div class="price-tag">$56.10</div>
  </article>
  <article class="category category--lashes">
    <h3>Lashes</h3>
    <div class="category-photo" role="img" aria-label="Pairs of false lashes arranged in their case"></div>
    <p>Lorem Ipsum is simply dummy text of the printing and typesetting industry.</p>
    <div class="price-tag">$56.10</div>
  </article>
</section>

<section class="highlights">
  <div class="highlight" style="left:87px">
    <svg class="highlight-icon" viewBox="0 0 72 72" aria-hidden="true">
      <rect x="8" y="28" width="56" height="34" rx="17" fill="var(--rose-icon)"/>
      <circle cx="20" cy="45" r="5" fill="var(--white)"/>
      <circle cx="36" cy="45" r="5" fill="var(--white)"/>
      <circle cx="52" cy="45" r="5" fill="var(--white)"/>
    </svg>
    <h4>Sponges</h4>
    <p>Morbi interdum mollis sapien. Sed ac risus. Phasellus lacinia, magna lorem ullamcorper.</p>
    <a class="btn-outline" href="#">Know More</a>
  </div>
  <div class="highlight" style="left:469px">
    <svg class="highlight-icon" viewBox="0 0 72 72" aria-hidden="true">
      <circle cx="36" cy="36" r="28" fill="none" stroke="var(--rose-icon)" stroke-width="5"/>
      <path d="M29 23 L51 36 L29 49 Z" fill="var(--rose-icon)"/>
    </svg>
    <h4>Tutorials</h4>
    <p>Morbi interdum mollis sapien. Sed ac risus. Phasellus lacinia, magna lorem ullamcorper.</p>
    <a class="btn-outline" href="#">Know More</a>
  </div>
  <div class="highlight" style="left:836px">
    <svg class="highlight-icon" viewBox="0 0 72 72" aria-hidden="true">
      <rect x="16" y="4" width="16" height="10" fill="var(--rose-icon)"/>
      <rect x="6" y="16" width="36" height="52" rx="8" fill="var(--rose-icon)"/>
      <rect x="12" y="32" width="24" height="18" fill="var(--white)"/>
      <path d="M46 66 C46 46 56 36 68 36 C68 54 58 66 46 66 Z" fill="var(--rose-icon)"/>
    </svg>
    <h4>Quality Products</h4>
    <p>Morbi interdum mollis sapien. Sed ac risus. Phasellus lacinia, magna lorem ullamcorper.</p>
    <a class="btn-outline" href="#">Know More</a>
  </div>
</section>

<section class="contact">
  <div class="contact-photo" role="img" aria-label="Woman in a grey shirt and jeans seated on a red stool in a dim studio"></div>
  <h2 class="contact-title">Get in Touch</h2>
  <span class="field-label" style="left:85px;top:110px">Name</span>
  <div class="field-box" style="left:87px;top:171px;width:489px;height:71px"></div>
  <span class="field-label" style="left:686px;top:110px">Email</span>
  <div class="field-box" style="left:629px;top:171px;width:487px;height:71px"></div>
  <span class="field-label" style="left:85px;top:274px">Message</span>
  <div class="field-box" style="left:87px;top:340px;width:1029px;height:235px"></div>
  <a class="btn-send" href="#">Send Message</a>
</section>

<footer class="site-footer">
  <div class="copyright">@2018. All Rights Reserved</div>
  <div class="social-links" aria-label="Social links"><span></span><span></span><span></span></div>
</footer>

</body>
</html>
```